Legal Service Estimated Retainer and Average Case Value

We need an 11x14 flyer that contains the standard retainers and average cost be case, both provided in documents, for each case type we handle. We need the information displayed, preferably in a way that makes the information readable but less troubling to a client shocked at price of litigation. We need one sheet with the retainers and average case value merged into one table.

Target Market(s)

Potential Clients

Font styles to use
Serif
Sans Serif

```html
<!DOCTYPE html>
<html lang="en">
<head>
<meta charset="utf-8">
<title>Fee &amp; Retainer Guide — The Law Office of Marcus T. Holloway</title>
<link rel="stylesheet" href="https://fonts.googleapis.com/css2?family=Barlow+Condensed:wght@400;500;600&family=Crimson+Pro:wght@400;500&display=swap">
<style>
  :root {
    --page-bg: #f2f2f2;
    --paper: #ffffff;
    --royal: #1d4aa0;
    --royal-soft: #4f7dc7;
    --slate: #363b52;
    --navy: #0a1540;
    --ink: #1b1d26;
    --band: #ececec;
    --row-alt: #ededed;
    --row: #f6f6f6;
    --sky: #b4cfeb;
  }
  * { box-sizing: border-box; margin: 0; padding: 0; }
  html, body { width: 1200px; height: 1200px; overflow: hidden; }
  body {
    background: var(--page-bg);
    font-family: "Barlow Condensed", "Arial Narrow", sans-serif;
    color: var(--ink);
    position: relative;
  }
  .flyer {
    position: absolute;
    left: 158px; top: 38px;
    width: 884px; height: 1125px;
    background: linear-gradient(to bottom, var(--paper) 0, var(--paper) 540px, var(--sky) 1000px, var(--sky) 100%);
    box-shadow: 0 4px 14px rgba(0,0,0,.25);
  }
  .masthead { position: relative; height: 120px; background: var(--paper); }
  .brand {
    position: absolute; left: 48px; top: 32px;
    display: flex; align-items: center; gap: 14px;
    color: var(--navy);
    font-family: "Crimson Pro", Georgia, serif; font-weight: 500;
  }
  .brand-mark { width: 48px; height: 56px; background: var(--navy); }
  .brand-name { line-height: 1; }
  .brand-name small { display: block; font-size: 12px; letter-spacing: .5px; margin-bottom: 3px; }
  .brand-name span { font-size: 27px; letter-spacing: .5px; }
  .tagline {
    position: absolute; right: 0; top: 0;
    width: 464px; height: 120px;
    background: var(--royal); color: #fff;
    font-family: "Crimson Pro", Georgia, serif; font-size: 24px; line-height: 1.15;
    padding: 30px 0 0 26px;
  }
  .intro {
    margin-top: 27px; height: 100px;
    background: var(--band);
    border-left: 7px solid var(--royal);
    padding: 20px 0 0 53px;
    font-size: 16px; line-height: 21px; color: #2a2a2a;
  }
  .fees {
    position: absolute; left: 61px; top: 272px; width: 771px;
    border-collapse: separate; border-spacing: 0;
  }
  .fees th {
    height: 43px; color: #fff; font-weight: 400;
    font-family: "Crimson Pro", Georgia, serif; font-size: 21px; letter-spacing: .5px;
    border-right: 4px solid var(--paper); border-bottom: 4px solid var(--paper);
  }
  .fees th:last-child { border-right: 0; }
  .col-case { background: var(--slate); width: 355px; }
  .col-avg { background: var(--royal-soft); width: 209px; }
  .col-ret { background: var(--royal); }
  .fees td { height: 45px; font-size: 17px; vertical-align: middle; }
  .fees tbody tr:nth-child(odd) td { background: var(--row-alt); }
  .fees tbody tr:nth-child(even) td { background: var(--row); }
  .fees tbody tr:last-child td { border-bottom: 3px solid var(--slate); }
  .case { padding-left: 18px; font-weight: 500; }
  .case::before { content: "•"; color: var(--royal); margin-right: 5px; }
  .fee { text-align: center; padding-right: 28px; }
  .ret { text-align: center; padding-right: 26px; }
  .tall td { height: 65px; vertical-align: top; padding-top: 12px; }
  .ret em { display: block; font-style: normal; color: var(--royal); font-size: 14px; font-weight: 500; margin-top: 2px; }
  .contact {
    position: absolute; left: 0; bottom: 38px; width: 100%; height: 84px;
    background: var(--paper);
  }
  .address { position: absolute; left: 70px; top: 14px; font-size: 14px; line-height: 18px; }
  .address strong { font-weight: 600; display: block; margin-left: 14px; }
  .address div { display: flex; align-items: center; gap: 4px; }
  .social {
    position: absolute; right: 0; top: 20px; width: 250px; height: 42px;
    border: 1.5px solid #555; border-right: 0; border-radius: 21px 0 0 21px;
    display: flex; align-items: center; gap: 15px; padding-left: 40px;
  }
  .social i { width: 27px; height: 27px; border-radius: 50%; background: var(--royal); display: block; }
  .web {
    position: absolute; left: 0; bottom: 0; width: 100%; height: 38px;
    background: var(--navy); color: #fff; text-align: center;
    font-family: "Crimson Pro", Georgia, serif; font-size: 19px; line-height: 38px; letter-spacing: .5px;
  }
</style>
</head>
<body>
<main class="flyer">
  <header class="masthead">
    <div class="brand">
      <div class="brand-mark"></div>
      <div class="brand-name"><small>THE LAW OFFICE OF</small><span>MARCUS T. HOLLOWAY</span></div>
    </div>
    <div class="tagline">Providing Quality Legal Counsel<br>to Clients Across Central Pennsylvania</div>
  </header>

  <section class="intro">
    In order for our clients to set expectations for legal fees, we provide the national average range of fees per case type.<br>
    These are only to provide you with an understanding of what other cases have cost clients in similar cases.<br>
    Please note these are not estimates nor guarantees of your own legal costs.
  </section>

  <table class="fees">
    <thead>
      <tr><th class="col-case">CASE TYPES</th><th class="col-avg">AVERAGE FEE</th><th class="col-ret">RETAINERS</th></tr>
    </thead>
    <tbody>
      <tr><td class="case">Custody Contempt/Modification</td><td class="fee">$5,000 - $8,000</td><td class="ret">$3,500</td></tr>
      <tr><td class="case">Custody Initial Order</td><td class="fee">$4,000 - $7,000</td><td class="ret">$3,000</td></tr>
      <tr><td class="case">Custody &amp; Support</td><td class="fee">$5,000 - $8,000</td><td class="ret">$3,000</td></tr>
      <tr><td class="case">Support</td><td class="fee">$2,000 - $4,000</td><td class="ret"></td></tr>
      <tr><td class="case">Divorce (3301c)</td><td class="fee">$1,500 - $3,000</td><td class="ret">$2,000</td></tr>
      <tr><td class="case">Divorce (3301d)</td><td class="fee">$2,000 - $3,000</td><td class="ret">$2,500</td></tr>
      <tr class="tall"><td class="case">Protection from Abuse (PFA)</td><td class="fee">$1,500 - $3,000</td><td class="ret">$2,000<em>Paid In Full</em></td></tr>
      <tr><td class="case">Divorce &amp; Support</td><td class="fee"></td><td class="ret">$3,000</td></tr>
      <tr><td class="case">Divorce &amp; Custody</td><td class="fee">$5,000 - $8,000</td><td class="ret">$3,500</td></tr>
      <tr><td class="case">Divorce &amp; Equitable Distribution</td><td class="fee">$6,000 - $10,000</td><td class="ret">$3,500</td></tr>
      <tr><td class="case">Divorce, Custody &amp; Support</td><td class="fee">$8,000 - $12,000</td><td class="ret">$3,500</td></tr>
      <tr><td class="case">Divorce, Equitable Distribution &amp; Custody</td><td class="fee">$10,000 - $15,000</td><td class="ret">$5,000</td></tr>
      <tr><td class="case">Divorce, Equitable Distribution &amp; Support</td><td class="fee">$8,000 - $12,000</td><td class="ret">$3,500</td></tr>
      <tr><td class="case">Divorce, Equitable Distribution, Custody &amp; Support</td><td class="fee">$12,000 - $15,000</td><td class="ret">$3,500</td></tr>
    </tbody>
  </table>

  <footer class="contact">
    <div class="address">
      <strong>The Law Office of Marcus T. Holloway</strong>
      <div>
        <svg width="11" height="13" viewBox="0 0 11 13" aria-hidden="true"><path d="M5.5 0C2.5 0 .5 2.2.5 5c0 3.5 5 8 5 8s5-4.5 5-8C10.5 2.2 8.5 0 5.5 0z" fill="#1d4aa0"/><circle cx="5.5" cy="5" r="1.8" fill="#fff"/></svg>
        2150 Ridgeview Avenue, Suite 210, Harrisburg, PA 17110
      </div>
      <div>
        <svg width="11" height="12" viewBox="0 0 11 12" aria-hidden="true"><path d="M2.2.5l1.8 2.6-1 1.3c.7 1.6 2 2.9 3.6 3.6l1.3-1 2.6 1.8-.9 2.2C5 10.7.3 6 .1 1.4z" fill="#1d4aa0"/></svg>
        (717) 555-0143
      </div>
    </div>
    <div class="social" aria-label="Social channels"><i></i><i></i><i></i><i></i></div>
  </footer>
  <div class="web">www.hollowayfamilylaw.com</div>
</main>
</body>
</html>
```